New business card design to go with our new logo

just want an eye-catching business card to go with our new logo. We are open to double sided or single sided. Just want it to have the following info on it. Whatever layout you think looks best.

First and Last Name
Title
Phone 801-555-0187
Address 312 W. Larkmoor Avenue Orem UT 84057
Email thecrew@meadowstailandkennel.example

Industry/Entity Type

Business

```html
<!DOCTYPE html>
<html lang="en">
<head>
<meta charset="utf-8">
<title>Meadows Tail &amp; Kennel — Business Card</title>
<link href="https://fonts.googleapis.com/css2?family=Roboto:wght@400;500&display=swap" rel="stylesheet">
<style>
  :root {
    --stage: #3a3a3c;
    --sky: #2aa3da;
    --sky-light: #4fb9e6;
    --orange: #f26d3d;
    --orange-light: #f7924f;
    --white: #ffffff;
  }
  html, body {
    margin: 0;
    width: 1200px;
    height: 896px;
    overflow: hidden;
    background: var(--stage);
    font-family: "Roboto", Arial, sans-serif;
  }
  .stage { position: relative; width: 1200px; height: 896px; }
  .card {
    position: absolute;
    top: 293px;
    width: 540px;
    height: 310px;
    border-radius: 18px;
    overflow: hidden;
    box-shadow: 0 10px 24px rgba(0,0,0,.45);
  }
  .card--front { left: 40px; background: linear-gradient(160deg, var(--sky) 0%, var(--sky-light) 100%); }
  .card--back { left: 620px; background: var(--white); }
  .card__art { position: absolute; inset: 0; }

  .brand {
    position: absolute;
    display: flex;
    align-items: center;
    gap: 12px;
    font-weight: 500;
    letter-spacing: .5px;
    white-space: nowrap;
  }
  .brand__dot { border-radius: 50%; flex: none; }
  .card--front .brand { left: 0; right: 0; top: 135px; justify-content: center; font-size: 30px; color: var(--white); }
  .card--front .brand__dot { width: 26px; height: 26px; background: var(--white); }
  .card--back .brand { left: 190px; top: 36px; font-size: 21px; color: var(--orange); }
  .card--back .brand__dot { width: 18px; height: 18px; background: var(--sky); }

  .person { position: absolute; left: 34px; top: 196px; color: var(--white); }
  .person__name { font-size: 21px; font-weight: 500; letter-spacing: 1px; margin: 0; }
  .person__title { font-size: 12px; margin: 2px 0 8px; opacity: .95; }
  .contact { list-style: none; margin: 0; padding: 0; font-size: 11.5px; line-height: 17px; }
  .contact li { display: flex; align-items: center; gap: 6px; }
  .contact svg { width: 9px; height: 9px; flex: none; }

  .address {
    position: absolute;
    right: 18px;
    top: 150px;
    text-align: right;
    color: var(--white);
    font-size: 12px;
    line-height: 17px;
  }
</style>
</head>
<body>
<main class="stage">

  <section class="card card--front" aria-label="Card front">
    <div class="brand"><span class="brand__dot"></span>Meadows Tail &amp; Kennel</div>
  </section>

  <section class="card card--back" aria-label="Card back">
    <svg class="card__art" viewBox="0 0 540 310" width="540" height="310" aria-hidden="true">
      <path d="M0 160 C200 150 380 100 540 30 L540 310 L0 310 Z" fill="var(--orange)"/>
      <path d="M0 171 C200 161 380 111 540 44 L540 310 L0 310 Z" fill="var(--orange-light)"/>
      <path d="M0 182 C200 172 380 122 540 58 L540 310 L0 310 Z" fill="var(--sky)"/>
      <path d="M500 52 C422 120 377 210 368 320" fill="none" stroke="var(--orange)" stroke-width="24"/>
      <path d="M490 56 C412 124 366 212 357 320" fill="none" stroke="var(--orange-light)" stroke-width="7"/>
    </svg>

    <div class="brand"><span class="brand__dot"></span>Meadows Tail &amp; Kennel</div>

    <div class="person">
      <p class="person__name">DANIEL REYES</p>
      <p class="person__title">Director</p>
      <ul class="contact">
        <li><svg viewBox="0 0 10 10"><path d="M2 1 L4 1 L4.6 3 L3.5 4 C4 5.3 4.8 6 6 6.5 L7 5.4 L9 6 L9 8 C5 8.5 1.5 5 2 1 Z" fill="#fff"/></svg>801-555-0187</li>
        <li><svg viewBox="0 0 10 10"><rect x="1" y="2" width="8" height="6" fill="none" stroke="#fff"/><path d="M1 2 L5 5.5 L9 2" fill="none" stroke="#fff"/></svg>thecrew@meadowstailandkennel.example</li>
        <li><svg viewBox="0 0 10 10"><circle cx="5" cy="5" r="4" fill="#fff"/></svg>www.meadowstailandkennel.example</li>
      </ul>
    </div>

    <div class="address">312 W. Larkmoor<br>Avenue<br>Orem UT 84057</div>
  </section>

</main>
</body>
</html>
```